Defense contractor needs a roll-up for an exhibition

The booth we have booked has only a size of 3m².
So this will be the centerpiece of the whole booth.
We need a roll-up that attracts visitors and at the same time it should contain already designed graphics. These graphics are giving visitors an overview of our system. So it is necessary to have them exposed in a height that the booth personal can conveniently point with its fingers at them.
For information about our company and product visit:
https://www.brightlanternoptics.com/
For designing you should use Adobe Illustrator and the templates provided in the zip file, to guarantee a perfect print.
I have supplied my business card that you can copy the logo. As the company logo will be already at the booth nearby the top of the roll-up, you should not place it there. It can be in the middle or at the bottom.
I have uploaded a picture of the booth. The roll up will be placed at the left of the screen and has a size of 80cm x 200cm

Defense

Defense

Serif

Colors
0054AA
0677BA
7BADD7
CADEEF
E8F1F8

• you must use the Adobe Illustrator template to have a good printing result
• company logo on the upper side of the roll-up

```html
<!DOCTYPE html>
<html lang="en">
<head>
<meta charset="utf-8">
<title>Bright Lantern Optics – LANTRIS Roll-up</title>
<link href="https://fonts.googleapis.com/css2?family=Play:wght@400;700&family=Saira+Condensed:wght@800&family=Source+Sans+3:wght@400;600;700&display=swap" rel="stylesheet">
<style>
  :root{
    --bg-deep:#0c0c0d;
    --bg-mid:#232325;
    --text:#ffffff;
    --text-soft:#e6e6e6;
    --accent:#f7d117;
    --rule:#f2f2f2;
    --illus-light:#d9d9d9;
    --illus-dark:#8a8a8a;
  }
  *{margin:0;padding:0;box-sizing:border-box}
  html,body{width:1200px;height:2824px;overflow:hidden;background:var(--bg-deep)}
  .rollup{
    position:relative;width:1200px;height:2824px;overflow:hidden;color:var(--text);
    font-family:"Source Sans 3",sans-serif;
    background:
      radial-gradient(ellipse 700px 600px at 780px 640px,#2e2e31 0%,transparent 70%),
      radial-gradient(ellipse 900px 700px at 700px 2000px,#2a2a2c 0%,transparent 70%),
      linear-gradient(180deg,var(--bg-mid) 0%,var(--bg-deep) 45%,#1a1a1b 100%);
  }
  .abs{position:absolute}
  .brand-name{
    left:84px;top:170px;font-family:"Saira Condensed",sans-serif;font-weight:800;
    font-size:90px;line-height:100px;color:var(--accent);letter-spacing:1px;text-transform:uppercase;
  }
  .heading{font-family:"Play",sans-serif;font-weight:700;letter-spacing:1.5px}
  .intro-title{left:72px;top:330px;font-size:38px;line-height:48px;width:620px}
  .intro-text{left:69px;top:496px;width:470px;font-size:22px;line-height:30px;color:var(--text-soft)}
  .intro-text strong{font-weight:700;color:var(--text)}
  .hero-illustration{left:444px;top:336px;width:708px;height:520px;border-radius:8px;
    background:radial-gradient(ellipse at 60% 60%,var(--illus-light) 0%,var(--illus-dark) 55%,transparent 75%);opacity:.55}
  .rule{height:2px;background:var(--rule)}
  .rule-1{left:72px;top:852px;width:624px}
  .rule-2{left:72px;top:1716px;width:1074px}
  .rule-3{left:366px;top:2292px;width:780px}
  .equip-title{left:69px;top:888px;font-size:37px;line-height:48px}
  .features-intro{left:72px;top:964px;width:1060px;font-size:22px;line-height:30px;color:var(--text-soft)}
  .features-intro strong{display:block;color:var(--text);font-weight:700}
  .feature-col{top:1124px;width:490px;display:flex;flex-direction:column;gap:12px}
  .feature-col.left{left:66px}
  .feature-col.right{left:630px}
  .feature{display:grid;grid-template-columns:42px 1fr;row-gap:8px}
  .feature svg{width:28px;height:28px;margin-top:2px}
  .feature h3{font-size:22px;line-height:30px;font-weight:700}
  .feature p{grid-column:2;font-size:22px;line-height:30px;color:var(--text-soft)}
  .mode{left:60px;width:1086px;display:grid;grid-template-columns:142px 1fr}
  .mode-duel{top:1756px}.mode-firing{top:1990px}.mode-driving{top:2140px}
  .mode h3{font-size:22px;line-height:30px;font-weight:700}
  .mode p{font-size:22px;line-height:30px;color:var(--text-soft)}
  .mode-icon{width:96px;height:80px;border-radius:6px;background:linear-gradient(180deg,#fff,#cfcfcf)}
  .mode-icon.svg{background:none}
  .debrief-title{right:54px;top:2326px;font-size:40px;line-height:52px}
  .debrief-text{left:778px;top:2400px;width:368px;font-size:22px;line-height:30px;text-align:justify;color:var(--text-soft)}
  .debrief-illustration{left:36px;top:2340px;width:708px;height:360px;
    background:linear-gradient(160deg,#efefef 0%,#a9a9a9 100%);clip-path:polygon(0 65%,30% 0,80% 0,100% 60%,100% 100%,0 100%);opacity:.85}
  .site{left:778px;top:2720px;font-size:20px;color:var(--text-soft)}
</style>
</head>
<body>
<main class="rollup">
  <div class="abs brand-name">Bright Lantern Optics</div>

  <h1 class="abs heading intro-title">Advanced Combat Training Systems for Realistic Combat Simulation</h1>
  <p class="abs intro-text"><strong>LANTRIS (Live Armor Network Tracking, Range &amp; Instrumentation System)</strong> allows for a modern approach to duel simulation, firing range training, armored vehicle driving training, and simulation debriefing through an integrated system of sensors, optics, and controls that give soldiers and instructors real-time, real-world vision and data.</p>
  <div class="abs hero-illustration" role="img" aria-label="Illustration of two battle tanks, three pop-up target stands and an instructor command truck with monitors and soldiers"></div>

  <div class="abs rule rule-1"></div>

  <h2 class="abs heading equip-title">Equip Your Fighting Force with Precision Training</h2>
  <p class="abs features-intro"><strong>Features of LANTRIS</strong>Fully deployed in 20 minutes or less, LANTRIS is uniquely designed to outfit armored vehicles and weapons systems including MBTs, armored IFVs and more regardless of manufacturer type with an array of advanced sensors and instrumentation for the most realistic and productive combat simulation achievable.</p>

  <div class="abs feature-col left">
    <div class="feature"><svg viewBox="0 0 28 28"><circle cx="14" cy="14" r="10" fill="none" stroke="#fff" stroke-width="3" stroke-dasharray="9 3"/></svg><h3>Remote-Control Functions</h3><p>Remote weapons blocking and camera control for integrated instruction management and safety</p></div>
    <div class="feature"><svg viewBox="0 0 28 28"><circle cx="14" cy="14" r="10" fill="none" stroke="#fff" stroke-width="3" stroke-dasharray="9 3"/></svg><h3>16 Camera Systems per vehicle</h3><p>Supports up to 16 remote-controlled cameras with pan, tilt, zoom, and thermal / night vision compatibility</p></div>
    <div class="feature"><svg viewBox="0 0 28 28"><circle cx="14" cy="14" r="10" fill="none" stroke="#fff" stroke-width="3" stroke-dasharray="9 3"/></svg><h3>Optics Camera</h3><p>Periscope optics camera placement allows for real-time instructor visibility of training grounds, targets, and crew performance</p></div>
    <div class="feature"><svg viewBox="0 0 28 28"><circle cx="14" cy="14" r="10" fill="none" stroke="#fff" stroke-width="3" stroke-dasharray="9 3"/></svg><h3>Vehicle Data</h3><p>Lead angles, ammunition types, speed, acceleration, turn indicators, temperature, and positions are shown on an interactive map</p></div>
  </div>
  <div class="abs feature-col right">
    <div class="feature"><svg viewBox="0 0 28 28"><circle cx="14" cy="14" r="10" fill="none" stroke="#fff" stroke-width="3" stroke-dasharray="9 3"/></svg><h3>Full Instructor Overview with Audio, Visuals, Vehicle Data, and Camera Control</h3><p>Live-stream radio, audio, visual, and sensor data overview with camera controls integrated with instructor command vehicle</p></div>
    <div class="feature"><svg viewBox="0 0 28 28"><circle cx="14" cy="14" r="10" fill="none" stroke="#fff" stroke-width="3" stroke-dasharray="9 3"/></svg><h3>Air-Conditioned Instructor Command Workstation</h3><p>Instructor workstation comfort control for optimal focus, precision, and command</p></div>
    <div class="feature"><svg viewBox="0 0 28 28"><circle cx="14" cy="14" r="10" fill="none" stroke="#fff" stroke-width="3" stroke-dasharray="9 3"/></svg><h3>Full Data Recording</h3><p>Audio, visual, and sensor data for debriefing, archiving, and performance metrics</p></div>
    <div class="feature"><svg viewBox="0 0 28 28"><circle cx="14" cy="14" r="10" fill="none" stroke="#fff" stroke-width="3" stroke-dasharray="9 3"/></svg><h3>All-Weather and All-Terrain</h3><p>Designed for durability and compatibility in any type of weather or terrain scenario</p></div>
  </div>

  <div class="abs rule rule-2"></div>

  <section class="abs mode mode-duel">
    <div class="mode-icon" role="img" aria-label="White tank silhouette icon"></div>
    <div><h3>Duel Simulation with LANTRIS</h3><p>LANTRIS is designed to surpass laser engagement system capabilities by achieving realistic training environments, hit detection, and soldier assessment and reaction to battle grounds and conditions. Instructors equipped with LANTRIS have the advantage of full overview, remote weapons blocking and camera control, and mediation among vehicle teams and units with real-time data delivered across multiple instructor workstations simultaneously for safe real-world training environments and results.</p></div>
  </section>
  <section class="abs mode mode-firing">
    <svg class="mode-icon svg" viewBox="0 0 96 96" aria-hidden="true"><circle cx="48" cy="48" r="30" fill="none" stroke="#fff" stroke-width="7"/><circle cx="48" cy="48" r="9" fill="none" stroke="#fff" stroke-width="6"/><path d="M48 6v22M48 68v22M6 48h22M68 48h22" stroke="#fff" stroke-width="7"/></svg>
    <div><h3>Firing Range Training with LANTRIS</h3><p>LANTRIS gives instructors complete visual, audio, and data oversight of firing range performance along with camera and weapons blocking control for optimal safety, ammunitions selection and conservation, target precision, and crew instruction.</p></div>
  </section>
  <section class="abs mode mode-driving">
    <div class="mode-icon" role="img" aria-label="Icon of a seated driver holding a steering wheel" style="width:70px;height:120px;margin-left:14px"></div>
    <div><h3>Driving Training with LANTRIS</h3><p>Vehicle teams with LANTRIS have increased vision, awareness, response times, and instructor assistance with control functions during driving training. LANTRIS offers cost-effective safety and driving training solutions in both combat and non-combat modes.</p></div>
  </section>

  <div class="abs rule rule-3"></div>

  <div class="abs debrief-illustration" role="img" aria-label="Illustration of a debriefing room with two wall screens and trainees seated at desks"></div>
  <h2 class="abs heading debrief-title">Debriefing with LANTRIS</h2>
  <p class="abs debrief-text">LANTRIS equips instructors with comprehensive data collection of training elements allowing for an immersive, insightful, and detailed debriefing process. All data contents can be easily recorded, edited, and archived for reference. LANTRIS features mobile container functionality for rapid deployment or a compact stationary workplace.</p>
</main>
</body>
</html>
```